Startseiten-Design für Software-Hersteller
Zielgruppe
Wir sind Softwarehersteller aus Berlin und unser Produkt ist eine Software zur Ortung von Fahrzeugen und zur Tourenplanung. Probleme die wir lösen - wo ist mein Auto gerade? Wo war mein Auto vor 1 Woche? Wie sollten meine Fahrer fahren, um möglichst effizient von A nach Z zu kommen?
Darüber hinaus verkaufen wir auch die für die Software notwendigen GPS-Geräte -> hier haben wir verschiedene Modelle im Angebot und ganz unterschiedliche Anschlussmöglichkeiten. Unsere Zielgruppe sind NUR Geschäftskunden: Handwerker, Bauunternehmen, Verlage, Winterdienste etc...
Aufgabenstellung
Vorab:
am besten ist das Projekt für jemanden geeignet, der schon mal eine affengeile Shop-Startseite gemacht hat - es soll mega professionell wirken und die Produkte sollen ins Auge springen. Wir benötigen nur eine Startseite -> Wichtig: den Shop haben wir bereits! Unsere aktuelle Seite findet ihr unter https://shop.wrx-systeme.de/ (ein absoluter Alptraum).
Gestalterisch könnt ihr euch echt austoben - ich denke wir entscheiden uns dann aus dem Bauch heraus. Wir sind generell auch Fans von etwas schlichtem - Hauptsache die Kunden klicken auf den Bestellen Button (dort verlinken wir dann den eigentlichen Shop). Programmiert wird das von unserem Dienstleister.
Die Startseite die wir möchten, sollte folgendes beinhalten:
- wenig Text -> dafür geile moderne Produktfotos mit ästhetischen Preisen (z. B. den Technohalle Shop finden wir hammer!)
- auf jeden Fall eine Zeile für unsere Gütesiegel
- selbstverständlich irgendwie an unsere Corporate Identity gehalten sein
- eine Art Pricing Tabelle beinhalten, in der wir die Unterschiede unserer verschiedenen Tarife verständlich an den Kunden bringen (wir haben sowas bereits auf unserer Website - > aber das sieht auch alles ziemlich Altbacken aus: https://www.wrx-systeme.de/gps-fahrzeugortung/gps-ortung-tourenplanung-tarifvergleich/).
- Wir haben insgesamt 4 Hardwaretypen + eine Menge Zubehör. Somit ist die Anzahl der Produkte recht übersichtlich -> rein für das Design könnt ihr euch die Bilder im Dateiupload ziehen und gern auch identische Fotos der Produkte für das Design nutzen.

```html
<!DOCTYPE html>
<html lang="de">
<head>
<meta charset="utf-8">
<title>RoutaFix – Startseite</title>
<link href="https://fonts.googleapis.com/css2?family=Poppins:wght@300;400;500&family=Roboto:wght@400;500;700;900&display=swap" rel="stylesheet">
<style>
  :root {
    --dark: #222222;
    --dark-2: #1b1b1b;
    --stage-light: #ececec;
    --stage-mid: #dcdcdc;
    --stage-shade: #c9c9c9;
    --card: #ffffff;
    --ink: #1a1a1a;
    --muted: #555555;
    --red: #d0263a;
    --text-light: #e9e9e9;
  }
  * { box-sizing: border-box; margin: 0; padding: 0; }
  html, body { width: 1200px; height: 800px; overflow: hidden; background: var(--dark); }
  .page { position: relative; width: 1200px; height: 800px; font-family: "Roboto", sans-serif; }

  .intro { position: absolute; top: 0; left: 0; width: 100%; height: 190px; background: var(--dark); text-align: center; color: var(--text-light); }
  .section-title { font-family: "Poppins", sans-serif; font-weight: 400; font-size: 17px; letter-spacing: .5px; padding-top: 40px; }
  .section-rule { width: 170px; height: 1px; background: #777; margin: 10px auto 0; position: relative; }
  .section-rule::after { content: ""; position: absolute; left: 50%; top: -1px; width: 30px; height: 3px; margin-left: -15px; background: #aaa; }
  .intro-copy { font-family: "Poppins", sans-serif; font-weight: 300; font-size: 14.5px; line-height: 1.75; margin-top: 24px; }

  .stage { position: absolute; top: 190px; left: 0; width: 100%; height: 460px; background: var(--stage-light); overflow: hidden; }
  .stage-shapes { position: absolute; inset: 0; }

  .product-card { position: absolute; width: 310px; height: 290px; background: var(--card); padding: 26px 24px 0; box-shadow: 0 2px 10px rgba(0,0,0,.08); }
  .card-1 { left: 60px; top: 110px; }
  .card-2 { left: 440px; top: 85px; }
  .card-3 { left: 810px; top: 60px; }

  .product-name { font-weight: 900; font-size: 27px; color: var(--ink); line-height: 1; letter-spacing: -.3px; }
  .product-tagline { font-size: 9.5px; font-weight: 500; color: var(--muted); margin-top: 5px; letter-spacing: .2px; }
  .feature-list { list-style: none; margin-top: 24px; }
  .feature-list li { font-size: 11px; color: #333; margin-bottom: 9px; white-space: nowrap; }
  .feature-list li::before { content: ">>"; color: var(--red); font-weight: 700; font-size: 9px; margin-right: 6px; }

  .price { position: absolute; right: 30px; top: 166px; color: var(--red); font-weight: 900; font-size: 38px; line-height: 1; white-space: nowrap; }
  .price .currency { font-size: 15px; color: #333; font-weight: 700; margin-right: 3px; }
  .product-button { position: absolute; left: 24px; top: 248px; border: 1.5px solid var(--red); color: var(--red); font-size: 9.5px; font-weight: 500; padding: 4px 12px; background: #fff; }

  .product-visual { position: absolute; border-radius: 10px; }
  .visual-device { left: 170px; top: 215px; width: 165px; height: 105px; background: linear-gradient(160deg, #4a4a4a, #1c1c1c); }
  .visual-tracker { left: 160px; top: 220px; width: 170px; height: 100px; background: linear-gradient(160deg, #3a3a3a, #141414); }
  .visual-phone { left: 235px; top: 105px; width: 95px; height: 180px; background: linear-gradient(180deg, #f4f4f4, #cfd6d2); border: 3px solid #333; border-radius: 8px; }

  .card-3 .price { right: auto; left: 120px; top: 178px; }
  .card-3 .product-button { top: 192px; }

  .tariffs { position: absolute; top: 650px; left: 0; width: 100%; height: 150px; background: var(--dark-2); text-align: center; color: var(--text-light); }
  .tariffs .section-title { padding-top: 40px; }
</style>
</head>
<body>
<main class="page">
  <section class="intro">
    <h2 class="section-title">BESSER GEHT'S NICHT</h2>
    <div class="section-rule"></div>
    <p class="intro-copy">RoutaFix ist selbsterklärend und leicht zu bedienen.<br>Innerhalb kürzester Zeit orten Sie Ihre Fahrzeuge ganz einfach vom Büro aus.</p>
  </section>

  <section class="stage">
    <svg class="stage-shapes" width="1200" height="460" viewBox="0 0 1200 460" aria-hidden="true">
      <polygon points="0,460 0,120 380,460" fill="var(--stage-mid)"/>
      <polygon points="600,460 1200,0 1200,460" fill="var(--stage-mid)"/>
      <polygon points="820,460 1200,170 1200,460" fill="var(--stage-shade)"/>
    </svg>

    <article class="product-card card-1">
      <h3 class="product-name">KOMPAKT MINI</h3>
      <p class="product-tagline">LOREM IPSUM DOLOR SIT AMET</p>
      <ul class="feature-list">
        <li>Lorem ipsum dolor sit amet</li>
        <li>Sit amet dolor ipsum amet lorem</li>
        <li>Super features!</li>
      </ul>
      <p class="price"><span class="currency">€</span>11,99</p>
      <span class="product-button">Zum Produkt</span>
      <div class="product-visual visual-device" role="img" aria-label="Produktfoto: schwarzes GPS-Ortungsgerät mit Kabelanschluss"></div>
    </article>

    <article class="product-card card-2">
      <h3 class="product-name">RX 250</h3>
      <p class="product-tagline">LOREM IPSUM DOLOR SIT AMET</p>
      <ul class="feature-list">
        <li>Lorem ipsum dolor sit amet</li>
        <li>Sit amet dolor ipsum amet lorem</li>
        <li>Super features!</li>
      </ul>
      <p class="price"><span class="currency">€</span>9,99</p>
      <span class="product-button">Zum Produkt</span>
      <div class="product-visual visual-tracker" role="img" aria-label="Produktfoto: kompakter schwarzer GPS-Tracker mit blauem Deckel"></div>
    </article>

    <article class="product-card card-3">
      <h3 class="product-name">ROUTAFIX GO!</h3>
      <p class="product-tagline">LOREM IPSUM DOLOR SIT AMET</p>
      <ul class="feature-list">
        <li>Lorem ipsum dolor sit amet</li>
        <li>Sit amet dolor ipsum amet lorem</li>
        <li>Super features!</li>
      </ul>
      <p class="price"><span class="currency">€</span>9,99</p>
      <span class="product-button">Zum Produkt</span>
      <div class="product-visual visual-phone" role="img" aria-label="Produktfoto: Smartphone mit geöffneter Ortungs-App"></div>
    </article>
  </section>

  <section class="tariffs">
    <h2 class="section-title">LEISTUNGSÜBERSICHT ROUTAFIX TARIFE</h2>
    <div class="section-rule"></div>
  </section>
</main>
</body>
</html>
```